Silverline Skills Institute

Our company needs a simple effective website with a clean design. We are working towards lowering the number of drownings that effect huge numbers each year. We will primarily link members to find education seminars, conferences and online material. With a forum to pose questions, have them answered by the community and moderated by staff members.

Target Market(s)

Swimming School Owners, Coaches, Parents and Community Groups

Industry/Entity Type

Education

Number of Pages Required

5+ page

Requirements
Must have
• A layout for all of the included pages. A good design for the forum. I will need to send this concept design to a coder for the final product.
Nice to have
• i would like to see an Olympic Swimming Pool incorporated into the options menu.

```html
<!DOCTYPE html>
<html lang="en">
<head>
<meta charset="utf-8">
<title>Silverline Skills Institute</title>
<link href="https://fonts.googleapis.com/css2?family=Roboto+Slab:wght@400;700&family=Open+Sans:wght@400;600&display=swap" rel="stylesheet">
<style>
:root{
  --blue:#1b87dc;
  --blue-dark:#1570bd;
  --ink:#333;
  --body:#555;
  --cream:#f3efe6;
  --footer:#1c1c1c;
  --white:#fff;
}
*{box-sizing:border-box;margin:0;padding:0}
html,body{width:762px;height:1200px;overflow:hidden}
body{position:relative;font-family:"Open Sans",sans-serif;color:var(--body);background:var(--white)}
.hero{position:absolute;left:0;top:0;width:762px;height:418px;
  background:
    radial-gradient(ellipse 140px 110px at 410px 250px,rgba(255,255,255,.35),transparent 70%),
    radial-gradient(ellipse 120px 120px at 690px 230px,rgba(255,255,255,.25),transparent 70%),
    radial-gradient(ellipse 260px 120px at 520px 300px,rgba(150,215,245,.5),transparent 75%),
    linear-gradient(180deg,#6cc2ee 0%,#37a2e2 35%,#2a8fd4 58%,#4e8bb0 78%,#8a9399 100%)}
.nav-panel{position:absolute;left:63px;top:0;width:149px;height:352px;background:var(--blue);
  clip-path:polygon(0 0,100% 0,100% 100%,0 94%)}
.brand{height:104px;background:var(--cream);display:flex;align-items:center;justify-content:center;gap:6px;padding:0 10px;
  clip-path:polygon(0 0,100% 0,100% 100%,50% 94%,0 100%)}
.brand-dot{width:12px;height:12px;border-radius:50%;background:var(--blue);flex:none}
.brand-name{font-family:"Roboto Slab",serif;font-weight:700;font-size:13px;line-height:1.2;color:var(--blue-dark)}
.menu{list-style:none;margin-top:13px}
.menu li{height:28.3px;display:flex;align-items:center;gap:10px;padding-left:16px;
  font-family:"Roboto Slab",serif;font-size:9.5px;color:var(--white);border-bottom:1px solid rgba(255,255,255,.15)}
.menu li:last-child{border-bottom:none}
.menu svg{width:10px;height:10px;fill:var(--white);flex:none}
.hero-title{position:absolute;left:238px;top:306px;font-family:"Roboto Slab",serif;font-weight:700;color:var(--white);line-height:1}
.hero-title .l1{font-size:31px;display:block}
.hero-title .l2{font-size:23px;display:block;margin-top:8px}
.arrows{position:absolute;left:237px;top:384px;display:flex;gap:6px}
.arrows span{width:20px;height:20px;border:1.5px solid rgba(255,255,255,.8);border-radius:50%;display:flex;align-items:center;justify-content:center}
.arrows svg{width:10px;height:10px;stroke:#fff;fill:none;stroke-width:1.6}

.welcome{position:absolute;left:0;top:418px;width:762px;height:244px;
  background:linear-gradient(90deg,#f4f8fb 0%,#eef2f4 55%,#f2ece4 100%)}
.welcome-art{position:absolute;left:80px;top:52px;width:88px;height:136px;
  background:radial-gradient(circle at 45% 65%,#3f8fd0 0%,#1d5d9e 60%,#123f70 100%);
  border-radius:50% 50% 50% 50% / 62% 62% 38% 38%}
.welcome h1{position:absolute;left:197px;top:36px;font-family:"Roboto Slab",serif;font-weight:700;font-size:25px;color:var(--ink)}
.welcome h1 em{font-style:normal;color:var(--blue)}
.welcome-text{position:absolute;left:198px;top:74px;width:494px;font-family:"Roboto Slab",serif;font-size:7.6px;line-height:14px;color:#444}
.welcome-text p+p{margin-top:6px}

.programs{position:absolute;left:0;top:662px;width:762px;height:340px;
  background:linear-gradient(180deg,#1a7fd6 0%,#2a92e4 50%,#1c80d6 100%)}
.card{position:absolute;top:104px;width:201px;height:192px;background:#f8f8f8;text-align:center}
.card .photo{position:absolute;left:40px;top:-66px;width:120px;height:120px;border-radius:50%;border:4px solid var(--blue)}
.card h2{position:absolute;left:0;right:0;top:70px;font-family:"Roboto Slab",serif;font-weight:400;font-size:12px;color:var(--ink)}
.card p{position:absolute;left:16px;right:16px;top:91px;font-size:7.3px;line-height:13px;color:#444}
.card .btn{position:absolute;left:62px;top:153px;width:76px;height:20px;border:1px solid #333;font-size:7.5px;color:#333;
  display:flex;align-items:center;justify-content:center;gap:4px}
.btn svg{width:8px;height:6px;fill:#333}

.footer{position:absolute;left:0;top:1002px;width:762px;height:168px;background:var(--footer);color:var(--white)}
.footer h3{position:absolute;top:31px;font-weight:400;font-size:10.5px;text-transform:uppercase;white-space:nowrap}
.col-blog{position:absolute;left:63px;top:0;width:150px}
.col-blog p{position:absolute;top:55px;width:150px;font-size:7px;line-height:12px}
.col-blog .date{position:absolute;top:97px;font-size:10px;color:var(--blue)}
.social{position:absolute;top:123px;display:flex;gap:3px}
.social span{width:16px;height:16px;border-radius:50%;background:var(--white);display:flex;align-items:center;justify-content:center}
.social svg{width:8px;height:8px;fill:none;stroke:#1c1c1c;stroke-width:1.3}
.col-news{position:absolute;left:247px;top:0;width:150px}
.col-news p{position:absolute;top:56px;width:150px;font-size:7px;line-height:12px}
.subscribe{position:absolute;top:89px;display:flex}
.subscribe .field{width:84px;height:26px;background:#fff;color:#444;font-size:7px;display:flex;align-items:center;padding-left:9px}
.subscribe .go{width:51px;height:26px;background:var(--blue);font-size:7px;font-weight:600;display:flex;align-items:center;justify-content:center}
.col-info{position:absolute;left:438px;top:0}
.col-info ul{position:absolute;top:55px;list-style:none;font-size:7.5px;line-height:15.2px;white-space:nowrap}
.col-contact{position:absolute;left:548px;top:0;width:200px}
.col-contact h3{top:33px}
.col-contact .addr{position:absolute;top:56px;font-size:8px;line-height:12.5px;white-space:nowrap}
.col-contact .row{position:absolute;left:0;display:flex;align-items:center;gap:10px;font-size:8.5px;white-space:nowrap}
.row svg{width:11px;height:11px;stroke:#fff;fill:none;stroke-width:1.2}
.bottom{position:absolute;left:0;top:1170px;width:762px;height:30px;background:var(--blue);color:var(--white);
  font-size:7.5px;display:flex;align-items:center;justify-content:center}
</style>
</head>
<body>

<section class="hero" role="img" aria-label="Photo of two smiling children in swim caps in a blue swimming pool">
  <nav class="nav-panel">
    <div class="brand"><span class="brand-dot"></span><span class="brand-name">Silverline Skills Institute</span></div>
    <ul class="menu">
      <li><svg viewBox="0 0 10 10"><path d="M5 1 0 5h1.5v4h2.5V6.5h2V9h2.5V5H10z"/></svg>Home</li>
      <li><svg viewBox="0 0 10 10"><circle cx="5" cy="3" r="2.3"/><path d="M1 10c0-3 1.8-4.3 4-4.3S9 7 9 10z"/></svg>About Us</li>
      <li><svg viewBox="0 0 10 10"><path d="M5 0 0 3h10zM1 4h1.5v4H1zm3.2 0h1.6v4H4.2zM7.5 4H9v4H7.5zM0 8.7h10V10H0z"/></svg>Community</li>
      <li><svg viewBox="0 0 10 10"><path d="M0 2h10v8H0zm1 3v4h8V5z"/></svg>Events</li>
      <li><svg viewBox="0 0 10 10"><path d="M0 0h5l5 5-5 5-5-5zm2 2.5a.8.8 0 1 0 0 .1z"/></svg>Why get involved</li>
      <li><svg viewBox="0 0 10 10"><path d="M1.5 0h5L9 2.5V10H1.5z"/></svg>Become Certified</li>
      <li><svg viewBox="0 0 10 10"><path d="M2 5h6v5H2zM3 5V3a2 2 0 0 1 4 0h-1a1 1 0 0 0-2 0v2z"/></svg>Login</li>
      <li><svg viewBox="0 0 10 10"><path d="M0 2h10v6H0zm1 1 4 3 4-3v-.2H1z"/></svg>Contact Us</li>
    </ul>
  </nav>
  <h2 class="hero-title"><span class="l1">WATER SAFETY</span><span class="l2">&amp; AQUATIC EDUCATION</span></h2>
  <div class="arrows">
    <span><svg viewBox="0 0 10 10"><path d="M8 5H2m3-3L2 5l3 3"/></svg></span>
    <span><svg viewBox="0 0 10 10"><path d="M2 5h6M5 2l3 3-3 3"/></svg></span>
  </div>
</section>

<section class="welcome">
  <div class="welcome-art" role="img" aria-label="Illustration of a water drop containing a globe"></div>
  <h1>WELCOME TO <em>SSI</em></h1>
  <div class="welcome-text">
    <p>Each year globally there are 372 000 people drowning everyday, from young children to victims of flood. According to a 2007 report released by Safe Shores Network, as many as 30,000 children between 0 and 14 years old die by drowning each year in China. That accounts for up to 60 percent of China's annual accidental child deaths, and the figures are climbing. If this tally isn't frightening enough think of the non fatal drownings that lead to permanent brain damage and disability.</p>
    <p>Spreading the message of water safety and education is important to help reduce this number and give everyone a fighting chance. There are many simple life saving skills and tips that can be spread with very little cost. Barriers on waterways, safe areas to leave children away from water, education in swimming, training in lifesaving techniques and most importantly education on the associated risks to young children around water.</p>
  </div>
</section>

<section class="programs">
  <article class="card" style="left:62px">
    <div class="photo" role="img" aria-label="Photo of a child in a straw hat playing with a paper boat at the water's edge" style="background:linear-gradient(160deg,#c9c2a6,#8c8a6c)"></div>
    <h2>Children Away From Water</h2>
    <p>Spreading the message of water safety and education is important to Become Ce d reduce this number and give everyone a fighting chance. There Log in are many simple life saving</p>
    <div class="btn">READ MORE <svg viewBox="0 0 8 6"><path d="M0 2.3h5V0l3 3-3 3V3.7H0z"/></svg></div>
  </article>
  <article class="card" style="left:280px">
    <div class="photo" role="img" aria-label="Photo of a mother and two young children in a pool with swim aids" style="background:linear-gradient(160deg,#6cc0ea,#2f8fcf)"></div>
    <h2>Education in Swimming</h2>
    <p>Spreading the message of water safety and education is important to Become Ce d reduce this number and give everyone a fighting chance. There Log in are many simple life saving</p>
    <div class="btn">READ MORE <svg viewBox="0 0 8 6"><path d="M0 2.3h5V0l3 3-3 3V3.7H0z"/></svg></div>
  </article>
  <article class="card" style="left:498px">
    <div class="photo" role="img" aria-label="Photo of a boy wearing a red life jacket outdoors" style="background:linear-gradient(170deg,#e6eef4 0%,#c7d5df 55%,#c8423a 100%)"></div>
    <h2>Training In Lifesaving Techniques</h2>
    <p>Spreading the message of water safety and education is important to Become Ce d reduce this number and give everyone a fighting chance. There Log in are many simple life saving</p>
    <div class="btn">READ MORE <svg viewBox="0 0 8 6"><path d="M0 2.3h5V0l3 3-3 3V3.7H0z"/></svg></div>
  </article>
</section>

<footer class="footer">
  <div class="col-blog">
    <h3>Latest Blog</h3>
    <p>Lorem ipsum dolor sit amet, consectetur adipiscing elit, sed do eiusmod tempor incididunt ut labore et dolore</p>
    <span class="date">Oct 15, 2016</span>
    <div class="social">
      <span><svg viewBox="0 0 8 8"><path d="M1 1.5h6v5H1zM1 1.5l3 2.5 3-2.5"/></svg></span>
      <span><svg viewBox="0 0 8 8"><path d="M1 1.5h6v4H3.5L2 7V5.5H1z"/></svg></span>
      <span><svg viewBox="0 0 8 8"><circle cx="4" cy="4" r="3"/><path d="M1 4h6M4 1c1.5 1.8 1.5 4.2 0 6M4 1c-1.5 1.8-1.5 4.2 0 6"/></svg></span>
      <span><svg viewBox="0 0 8 8"><path d="M3 5 5 3M2.5 4 1.5 5a1 1 0 0 0 1.5 1.5l1-1M5.5 4l1-1A1 1 0 0 0 5 1.5l-1 1"/></svg></span>
    </div>
  </div>
  <div class="col-news">
    <h3>Join Our Newsletter</h3>
    <p>Excepteur sint occaecat cupidatat non proident, sunt in culpa qui</p>
    <div class="subscribe"><span class="field">Enter Name</span><span class="go">SUBSCRIBE</span></div>
  </div>
  <div class="col-info">
    <h3>Information</h3>
    <ul><li>about us</li><li>Community</li><li>Events</li><li>Why get involved</li><li>Become Certifie</li></ul>
  </div>
  <div class="col-contact">
    <h3>Contact Us</h3>
    <div class="addr">Silverline Skills Institute<br>4120 LK&nbsp; Harborview</div>
    <div class="row" style="top:91px"><svg viewBox="0 0 12 12"><path d="M2 1l2 0 1 3-1.5 1a6 6 0 0 0 3.5 3.5L8 7l3 1v2a1 1 0 0 1-1 1A9 9 0 0 1 1 2a1 1 0 0 1 1-1z"/></svg>+1 555 0142 7730</div>
    <div class="row" style="top:108px"><svg viewBox="0 0 12 12"><path d="M1 2.5h10v7H1zM1 2.5l5 4 5-4"/></svg>hello@silverlineskills.org</div>
  </div>
</footer>
<div class="bottom">Copyright©2016 Silverline Skills Institute .All Rights Reserved.</div>

</body>
</html>
```